DOUBLE SIDED BROCHURE NEEDED TO PROMOTE DOCTOR

I need a double sided DL size (99mm x 210mm) brochure, promoting a doctor seeing patients in a new area.

I want something professional. I have included the relevant information. I would also like the Dr's picture somwhere in the brochure, with a professional background. I wish to print these tomorrow, so i will pick a winner within 14 hours of posting this ad.

I have included an example of a brochures design that I recently saw, and its definietly a good starting point.

Medical

```html
<!DOCTYPE html>
<html lang="en">
<head>
<meta charset="utf-8">
<title>Idris Halven – General, Breast &amp; Endocrine Surgeon</title>
<link rel="stylesheet" href="https://fonts.googleapis.com/css2?family=Permanent+Marker&family=Questrial&display=swap">
<style>
  :root {
    --sky-top: #a9d6f2;
    --sky-bottom: #eef7fb;
    --ink-teal: #0f4b4a;
    --band-light: #4aa3a0;
    --panel-top: #17605f;
    --panel-mid: #1d5766;
    --panel-bottom: #3b6c77;
    --footer: #1b6366;
    --footer-edge: #2c7a7b;
    --text-light: #eef6f6;
    --photo-light: #9c8c80;
    --photo-dark: #1b2230;
  }
  html, body {
    margin: 0;
    padding: 0;
    width: 1200px;
    height: 2539px;
    overflow: hidden;
    background: #ffffff;
  }
  .brochure {
    position: relative;
    width: 1200px;
    height: 2539px;
    overflow: hidden;
    font-family: "Questrial", "Century Gothic", sans-serif;
  }
  .backdrop {
    position: absolute;
    inset: 0;
    width: 1200px;
    height: 2539px;
  }
  .headline {
    position: absolute;
    left: 70px;
    top: 46px;
    margin: 0;
    color: var(--ink-teal);
    font-weight: 400;
  }
  .headline .name {
    display: block;
    font-size: 108px;
    line-height: 110px;
  }
  .headline .specialty {
    display: block;
    margin-top: 42px;
    font-size: 112px;
    line-height: 113px;
  }
  .greeting {
    position: absolute;
    left: 30px;
    top: 1192px;
    margin: 0;
    font-family: "Permanent Marker", cursive;
    font-weight: 400;
    font-size: 66px;
    letter-spacing: 2px;
    color: #ffffff;
  }
  .announcement {
    position: absolute;
    left: 86px;
    width: 1090px;
    margin: 0;
    font-size: 57px;
    line-height: 86px;
    color: var(--text-light);
  }
  .announcement.intro { top: 1290px; }
  .announcement.promise { top: 1684px; }
  .clinic-details {
    position: absolute;
    left: 0;
    top: 2232px;
    width: 1200px;
    text-align: center;
    color: #ffffff;
  }
  .clinic-details p { margin: 0; }
  .clinic-details .label {
    font-size: 46px;
    line-height: 56px;
    font-weight: 700;
  }
  .clinic-details .value {
    font-size: 44px;
    line-height: 54px;
  }
  .clinic-details .referral {
    font-size: 50px;
    line-height: 60px;
    font-weight: 700;
  }
</style>
</head>
<body>
<div class="brochure">
  <svg class="backdrop" viewBox="0 0 1200 2539" xmlns="http://www.w3.org/2000/svg">
    <defs>
      <linearGradient id="sky" x1="0" y1="0" x2="0" y2="1">
        <stop offset="0" stop-color="var(--sky-top)"/>
        <stop offset="1" stop-color="var(--sky-bottom)"/>
      </linearGradient>
      <linearGradient id="portrait" x1="0" y1="0" x2="0" y2="1">
        <stop offset="0" stop-color="var(--photo-light)"/>
        <stop offset="0.35" stop-color="#6f6a70"/>
        <stop offset="1" stop-color="var(--photo-dark)"/>
      </linearGradient>
      <linearGradient id="panel" x1="0" y1="0" x2="0" y2="1">
        <stop offset="0" stop-color="var(--panel-top)"/>
        <stop offset="0.55" stop-color="var(--panel-mid)"/>
        <stop offset="1" stop-color="var(--panel-bottom)"/>
      </linearGradient>
    </defs>

    <rect class="sky" width="1200" height="2539" fill="url(#sky)"/>

    <polygon class="accent-band" points="0,890 930,1320 0,1320" fill="var(--band-light)" opacity="0.85"/>

    <path class="portrait" d="M620,520 Q620,230 900,230 Q1200,230 1200,520 L1200,1150 L900,1310 L620,1217 Z"
          fill="url(#portrait)" role="img"
          aria-label="Portrait photograph of the surgeon in a dark suit jacket and checked shirt"/>

    <polygon class="content-panel" points="0,1010 900,1310 1200,1150 1200,2170 0,2170" fill="url(#panel)"/>

    <polygon class="footer-edge" points="18,2158 1200,2158 1200,2182 0,2182" fill="var(--footer-edge)"/>
    <rect class="footer" x="0" y="2182" width="1200" height="357" fill="var(--footer)"/>
  </svg>

  <h1 class="headline">
    <span class="name">Idris<br>Halven</span>
    <span class="specialty">General,<br>Breast &amp;<br>Endocrine<br>Surgeon</span>
  </h1>

  <h2 class="greeting">DEAR DOCTORS,</h2>

  <p class="announcement intro">We are pleased to<br>announce that Dr. Idris Halven is now<br>consulting in Seabreeze, seeing<br>public and private patients.</p>

  <p class="announcement promise">Guaranteed appointment within<br>two weeks, with patients having the<br>option of surgery at Coastal Health<br>Campus, Southgate Hospital or St.<br>Brennan Westfield.</p>

  <div class="clinic-details">
    <p class="label">Seabreeze Clinic:</p>
    <p class="value">42 Kestrel Road Seabreeze WA 6999.</p>
    <p class="label">Phone</p>
    <p class="value">1300 000 123</p>
    <p class="referral">Please send all referrals by fax to (08) 5550 1234</p>
  </div>
</div>
</body>
</html>
```